New Product Launch! Nothing on the market like it.

Incorporate the tag line ' New Day | New Year | New Corvane. Progress starts with Lumetta'.
2 infographs 1) All Weather2) UV Resistant- Position both topics as 'what that means'. For example, we can make this claim because we did the testing. A lot of our competitors make these claims and should not, nor do they perform anywhere close to Lumetta.
For the All Weather- Use graphics for each stage of temperature testing that look weather related; snow flake, oven, water, freezer, thermometer. I also want to communicate that after all that testing the bond strength of Lumetta stayed intact.
UV resistance, similar- competitors make UV claims, NONE come close to our performance nor have any products been subjected to these kinds of tests. I want to include that Lumetta Resists cracking, yellowing, and delamination even after years of continuous UV bombardment. This exceptional performance ensures long-term aesthetic and functional reliability in applications, and sustained UV exposure without compromising bond performance or appearance (or something similar). Would also like to include the tag line, 'Progress starts with Lumetta'.
Please use the attached deck to coordinate the All Weather and UV Resistance Claims to the testing.
All Weather- Engineered for both indoor and outdoor applications without compromising reliability under any conditions. Tested to ASTM D1183-03, subjected to multiple rounds of 230 hours of testing. Ambient Cure-64 hours | 71°C oven-48 hours | 23°C submerged in Water-48 hours | -10°C freezer- 8 hours | 38.5°C oven- 64 hours. The bond strength was barely affected.
High UV Resistance- Maintains color and integrity in sunlight where standard adhesives discolor or degrade over time. Resists cracking, yellowing, and delamination even after years of continuous use and exposure. 10X Less Yellowing- exposed to 100 hrs of UV in 20hr increments using a UVA 340 0- simulating direct noon sun, in accordance to ISO 4892-3- which is equivalent to 1 year under the florida sun. Lumetta measures a 1.5∆E while competitors read 11∆E

Target Market(s)

Fabricators (indoor/outdoor countertop) and Distributors

Industry/Entity Type

Subcontractor and Distributor

Colors
EE7325
F08F49
F5BC92
FAE3D3
FDF4ED

Requirements
Must have
• 2 infographs

```html
<!DOCTYPE html>
<html lang="en">
<head>
<meta charset="utf-8">
<title>All-Weather Performance</title>
<link rel="stylesheet" href="https://fonts.googleapis.com/css2?family=Archivo:wdth,wght@62..125,100..900&family=Red+Hat+Display:wght@400;500;700;800&display=swap">
<style>
  :root {
    --bg: #F9AE45;
    --card: #FEF3EC;
    --orange: #E07024;
    --amber: #F5AC3E;
    --rust: #9A4420;
    --ink: #3A2A22;
    --cream: #FDF4ED;
  }
  * { margin: 0; padding: 0; box-sizing: border-box; }
  html, body { width: 1200px; height: 925px; overflow: hidden; background: var(--bg); }
  .canvas { position: relative; width: 1200px; height: 925px; background: var(--bg); font-family: "Red Hat Display", sans-serif; }
  .card {
    position: absolute; left: 96px; top: 90px; width: 1007px; height: 745px;
    background: var(--card); box-shadow: 0 6px 18px rgba(120, 60, 10, 0.25);
  }
  .abs { position: absolute; }
  .title {
    left: 160px; top: 134px; font-family: "Archivo", sans-serif; font-stretch: 125%;
    font-variation-settings: "wdth" 125; font-weight: 800; font-size: 56px; line-height: 49px;
    color: var(--orange); letter-spacing: -0.5px;
  }
  .subtitle { left: 163px; top: 236px; font-size: 21px; line-height: 24.5px; color: var(--ink); font-weight: 400; }
  .divider { left: 163px; top: 302px; width: 874px; height: 1px; background: var(--rust); }
  .tagline {
    right: 163px; top: 144px; text-align: right; font-family: "Archivo", sans-serif;
    font-variation-settings: "wdth" 125; font-weight: 800; font-size: 18px; line-height: 19.5px; color: var(--ink);
  }
  .tagline .promise { display: block; margin-top: 8px; color: var(--rust); }
  .hub { left: 446px; top: 354px; width: 310px; height: 310px; border-radius: 50%; background: var(--orange); }
  .badge { width: 78px; height: 78px; border-radius: 50%; display: flex; align-items: center; justify-content: center; box-shadow: 0 4px 8px rgba(120, 60, 10, 0.2); }
  .badge--dark { background: var(--rust); }
  .badge--light { background: var(--amber); }
  .badge svg { width: 56px; height: 56px; fill: none; stroke: #fff; stroke-width: 2.6; stroke-linecap: round; stroke-linejoin: round; }
  .stat { font-size: 17.5px; line-height: 23px; color: var(--ink); text-transform: uppercase; }
  .stat--left { text-align: right; }
  .stat h3 { font-weight: 800; font-size: 20.5px; line-height: 26px; color: var(--rust); margin-bottom: 0; }
  .stat b { font-weight: 800; }
  .stat--tight { line-height: 19px; }
  .band {
    left: 211px; top: 715px; width: 778px; height: 60px; background: var(--orange);
    color: var(--cream); text-align: center; text-transform: uppercase;
  }
  .band .lead { font-size: 12.5px; padding-top: 12px; line-height: 14px; letter-spacing: 0.2px; }
  .band .claim { font-size: 19.5px; font-weight: 800; line-height: 24px; margin-top: 2px; }
</style>
</head>
<body>
<div class="canvas">
  <div class="card"></div>

  <h1 class="abs title">ALL–WEATHER<br>PERFORMANCE</h1>
  <p class="abs subtitle">Engineered for both indoor and outdoor applications<br>without compromising reliability under any conditions</p>
  <p class="abs tagline">NEW DAY<br>NEW YEAR<br>NEW CORVANE<span class="promise">PROGRESS STARTS WITH<br>LUMETTA</span></p>
  <div class="abs divider"></div>

  <div class="abs hub" role="img" aria-label="Weather scene illustration: sun, cloud with rain and snow, and flames"></div>

  <!-- badges -->
  <div class="abs badge badge--dark" style="left:443px;top:359px">
    <svg viewBox="0 0 56 56"><path d="M28 6v44M9 17l38 22M9 39l38-22M22 8l6 6 6-6M22 48l6-6 6 6M7 23l8-2-2-8M49 33l-8 2 2 8M7 33l8 2-2 8M49 23l-8-2 2-8"/></svg>
  </div>
  <div class="abs badge badge--light" style="left:674px;top:359px">
    <svg viewBox="0 0 56 56"><path d="M24 9C18 19 12 26 12 34a12 12 0 0 0 24 0c0-8-6-15-12-25z"/><path d="M18 34a6 6 0 0 0 6 6"/><path d="M38 14c-3 5-5 8-5 11a5 5 0 0 0 10 0c0-3-2-6-5-11z"/></svg>
  </div>
  <div class="abs badge badge--light" style="left:409px;top:470px">
    <svg viewBox="0 0 56 56"><path d="M22 33V12a5 5 0 0 1 10 0v21a9 9 0 1 1-10 0z"/><circle cx="27" cy="40" r="3.5"/><path d="M27 20v16M37 14h6M37 20h6M37 26h6M37 32h6"/></svg>
  </div>
  <div class="abs badge badge--dark" style="left:712px;top:470px">
    <svg viewBox="0 0 56 56"><circle cx="28" cy="28" r="11"/><path d="M28 6v6M28 44v6M6 28h6M44 28h6M12 12l4 4M40 40l4 4M12 44l4-4M40 16l4-4M34 33a7 7 0 0 0 1-6"/></svg>
  </div>
  <div class="abs badge badge--dark" style="left:443px;top:582px">
    <svg viewBox="0 0 56 56"><path d="M10 46V30a18 18 0 0 1 36 0v16M7 46h42M22 8h12v5H22zM16 46V31a12 12 0 0 1 24 0v15"/><path d="M28 42c-4 0-6-3-5-6 1-2 3-3 3-6 3 2 6 5 6 8s-1 4-4 4z"/></svg>
  </div>
  <div class="abs badge badge--light" style="left:674px;top:582px">
    <svg viewBox="0 0 56 56"><path d="M12 24a17 17 0 0 1 30-9M44 32a17 17 0 0 1-30 9"/><path d="M36 14h7V7M20 42h-7v7"/><path d="M25 31V19a3 3 0 0 1 6 0v12a5 5 0 1 1-6 0z"/></svg>
  </div>

  <!-- left stats -->
  <div class="abs stat stat--left" style="right:777px;top:361px">
    <h3>Snowflake</h3><b>–10°C</b> Freezer<br><b>08</b> Hours
  </div>
  <div class="abs stat stat--left" style="right:814px;top:472px">
    <h3>Thermometer</h3>Ambient Cure<br><b>64</b> Hours
  </div>
  <div class="abs stat stat--left" style="right:777px;top:584px">
    <h3>Oven / Heat Waves</h3><b>71°C</b> Oven<br><b>48</b> Hours
  </div>

  <!-- right stats -->
  <div class="abs stat" style="left:773px;top:358px">
    <h3>Water Droplet</h3><b>23°C</b> Water Immersion<br><b>48</b> Hours
  </div>
  <div class="abs stat" style="left:810px;top:472px">
    <h3>Sun + Heat</h3><b>38.5°C</b> Oven<br><b>64</b> Hours
  </div>
  <div class="abs stat stat--tight" style="left:773px;top:588px">
    <h3>ASTM D1183–03</h3><b>230+</b> Hours of Cyclic<br>Temperature Testing
  </div>

  <div class="abs band">
    <p class="lead">After repeated exposure to heat, cold, moisture, and freezing</p>
    <p class="claim">Lumetta’s bond strength remained intact</p>
  </div>
</div>
</body>
</html>
```